International tradind company needs a professional Business Card

We are an international trading company and we need a business card for our CEO and employers so they can give it away in their meetings and while networking.
We want the card design quality to cause an immediate "wow" and we count on you to do that!

key-words and concepts to communicate: trustworthiness, ethics, sucess, modern, global business, networking

Our favorite colours are blue and grey but we are open to suggestions.

It would be recommended that our logo was part of the card. You can see it in www.veldoranexus.com . We also would like the following info on the card:
Name
position in the company
cell phone and personal email

Industry/Entity Type

Business

```html
<!DOCTYPE html>
<html lang="en">
<head>
<meta charset="utf-8">
<title>Veldora Nexus — Business Card</title>
<link href="https://fonts.googleapis.com/css2?family=Open+Sans:wght@400&family=Arimo:wght@400;700&display=swap" rel="stylesheet">
<style>
  :root {
    --navy: #1a1750;
    --navy-light: #27386c;
    --ink: #15124a;
    --sky: #4a86c0;
    --text-grey: #4a4a4a;
    --stage-light: #f2f2f2;
    --stage-dark: #a9a9a9;
    --white: #ffffff;
  }
  * { margin: 0; padding: 0; box-sizing: border-box; }
  html, body { width: 1200px; height: 1000px; overflow: hidden; }
  body {
    position: relative;
    background: radial-gradient(ellipse 75% 70% at 45% 45%, var(--stage-light) 0%, #dcdcdc 60%, var(--stage-dark) 100%);
    font-family: "Arimo", Arial, sans-serif;
  }
  .brand-name {
    font-family: "Open Sans", "Myriad Pro", sans-serif;
    font-weight: 400;
    color: var(--ink);
    display: flex;
    align-items: center;
    white-space: nowrap;
  }
  .brand-name .brand-dot {
    border-radius: 50%;
    background: var(--sky);
    flex: none;
  }
  .logo-showcase {
    position: absolute; left: 62px; top: 228px;
    font-size: 40px; gap: 22px;
  }
  .logo-showcase .brand-dot { width: 90px; height: 90px; }
  .card {
    position: absolute;
    width: 593px; height: 383px;
    background: var(--white);
    box-shadow: 0 18px 14px -10px rgba(0,0,0,0.45);
    overflow: hidden;
  }
  .card svg.card-waves { position: absolute; inset: 0; width: 100%; height: 100%; }
  .card-front { left: 518px; top: 64px; }
  .card-front .brand-name {
    position: absolute; left: 66px; top: 140px;
    font-size: 46px; gap: 28px;
  }
  .card-front .brand-dot { width: 110px; height: 110px; }
  .card-back { left: 517px; top: 544px; }
  .card-back .brand-name {
    position: absolute; right: 36px; top: 32px;
    font-size: 24px; gap: 12px;
  }
  .card-back .brand-dot { width: 56px; height: 56px; }
  .contact {
    position: absolute; left: 35px; top: 31px;
    font-size: 20px; line-height: 24px; color: var(--text-grey);
  }
  .contact .role { color: var(--sky); margin-bottom: 24px; }
  .office {
    position: absolute; right: 35px; top: 252px;
    text-align: right; color: var(--white);
    font-size: 19px; line-height: 24px; font-style: normal;
  }
  .office .office-name { font-weight: 700; font-size: 21px; }
</style>
</head>
<body>

<div class="brand-name logo-showcase"><span class="brand-dot"></span>Veldora Nexus</div>

<section class="card card-front">
  <svg class="card-waves" viewBox="0 0 593 383" preserveAspectRatio="none" aria-hidden="true">
    <defs>
      <linearGradient id="bandFront" x1="0" y1="0" x2="1" y2="0">
        <stop offset="0" stop-color="#2a3a6e"/><stop offset="0.3" stop-color="#1a1750"/><stop offset="1" stop-color="#1a1750"/>
      </linearGradient>
      <linearGradient id="bandFrontLow" x1="0" y1="0" x2="1" y2="0">
        <stop offset="0" stop-color="#1a1750"/><stop offset="0.6" stop-color="#1a1750"/><stop offset="1" stop-color="#29396d"/>
      </linearGradient>
      <linearGradient id="silverTop" x1="0" y1="0" x2="1" y2="0">
        <stop offset="0" stop-color="#6a6a6a"/><stop offset="0.6" stop-color="#d8d8d8"/><stop offset="1" stop-color="#ffffff"/>
      </linearGradient>
      <linearGradient id="silverLow" x1="0" y1="0" x2="1" y2="0">
        <stop offset="0" stop-color="#ffffff"/><stop offset="0.5" stop-color="#cfcfcf"/><stop offset="1" stop-color="#555555"/>
      </linearGradient>
    </defs>
    <path d="M0 0 H593 V44 C520 70 440 94 330 96 C220 98 100 84 0 96 Z" fill="url(#silverTop)"/>
    <path d="M0 0 H593 V36 C520 62 440 86 330 88 C220 90 100 76 0 86 Z" fill="url(#bandFront)"/>
    <path d="M0 322 C90 288 200 266 320 266 C450 266 520 280 593 270 V383 H0 Z" fill="url(#silverLow)"/>
    <path d="M0 330 C90 296 200 274 320 274 C450 274 520 288 593 280 V383 H0 Z" fill="url(#bandFrontLow)"/>
  </svg>
  <div class="brand-name"><span class="brand-dot"></span>Veldora Nexus</div>
</section>

<section class="card card-back">
  <svg class="card-waves" viewBox="0 0 593 383" preserveAspectRatio="none" aria-hidden="true">
    <defs>
      <linearGradient id="bandBack" x1="0" y1="0" x2="1" y2="0">
        <stop offset="0" stop-color="#1a1750"/><stop offset="0.6" stop-color="#1a1750"/><stop offset="1" stop-color="#29396d"/>
      </linearGradient>
      <linearGradient id="silverBack" x1="0" y1="0" x2="1" y2="0">
        <stop offset="0" stop-color="#ffffff"/><stop offset="0.5" stop-color="#cfcfcf"/><stop offset="1" stop-color="#555555"/>
      </linearGradient>
    </defs>
    <path d="M0 228 C90 198 200 182 320 182 C450 182 520 192 593 184 V383 H0 Z" fill="url(#silverBack)"/>
    <path d="M0 238 C90 208 200 192 320 192 C450 192 520 202 593 194 V383 H0 Z" fill="url(#bandBack)"/>
  </svg>
  <div class="contact">
    <p class="person-name">Name Surname</p>
    <p class="role">CEO &amp; Employers</p>
    <p class="phone">M 555-0142718</p>
    <p class="email">E ceo@veldoranexus.com</p>
  </div>
  <div class="brand-name"><span class="brand-dot"></span>Veldora Nexus</div>
  <address class="office">
    <p class="office-name">Veldora Nexus</p>
    <p>Rua das Flores Altas, 18, 2o Esq</p>
    <p>1200-104 Lisboa</p>
    <p>Portugal</p>
  </address>
</section>

</body>
</html>
```